vantrel works cybersecurity website design and development

website design and development for a cybersecurity company. we have a logo and would like site to suit logo colors and look
cybersecurity website should be secure and look professional
main example of site we want to use: https://www.morvisquad.example/
site should be usable on tablet and phones

For each design proposal, please could you provide details of what language you'll use to code the website.

Target Market(s)

insurance companies, financial institutions, private SME, Africa and Europe

Coding

Coded - Design and coding required

Number of Pages Required

5+ page

Requirements
Must have
• 9 Pages:
Home
About us
Contacts
Partners
Blog
Services
( consulting, vulnerability assessment, information systems security audit, ISO compliance, Penetration testing, security awareness training, social engineering test, protection against DDoS, procurement )
Resources
Technologies
Careers
Nice to have
• nice to have all services have their own pages.
design based on logo colors and look

please provide what will be use to code the website

```html
<!DOCTYPE html>
<html lang="en">
<head>
<meta charset="utf-8">
<title>Vantrel Works — Cyber Security</title>
<link rel="stylesheet" href="https://fonts.googleapis.com/css2?family=Libre+Baskerville:wght@700&family=Poppins:wght@400;500;600&display=swap">
<style>
:root{
  --blue:#2b3597;
  --blue-deep:#1c1f8f;
  --ink:#222;
  --muted:#777;
  --light:#f5f5f5;
  --footer:#333;
  --green:#3cbf4a;
  --white:#fff;
}
*{box-sizing:border-box;margin:0;padding:0}
html,body{width:1200px;height:4345px;overflow:hidden}
body{font-family:"Poppins",sans-serif;color:var(--ink);background:var(--white);position:relative}
.serif{font-family:"Libre Baskerville",serif;font-weight:700}
section,header,footer{position:absolute;left:0;width:1200px}
.abs{position:absolute}
.btn{position:absolute;display:flex;align-items:center;justify-content:center;border-radius:30px;font-size:12px;font-weight:600}
.btn-blue{background:var(--blue);color:var(--white)}
.eyebrow{font-size:15px;color:#444}
.para{font-size:14px;line-height:23px;color:var(--muted)}

/* hero */
.hero{top:0;height:591px;background:linear-gradient(110deg,#0b127a 0%,#101ca8 45%,#1a36d6 75%,#0d1a9c 100%);color:var(--white);overflow:hidden}
.hero-art{position:absolute;right:0;top:0;width:560px;height:591px;background:radial-gradient(circle at 70% 45%,rgba(90,140,255,.45),rgba(20,40,200,0) 65%)}
.topbar{position:absolute;top:0;left:0;width:1200px;height:34px;border-bottom:1px solid rgba(255,255,255,.18);font-size:11px}
.topbar span{position:absolute;top:10px}
.social{position:absolute;display:flex;gap:10px}
.social i{width:10px;height:10px;border-radius:50%;background:currentColor;display:block}
.brand{position:absolute;display:flex;align-items:center;gap:8px;font-size:17px;font-weight:600}
.brand b{width:30px;height:30px;border-radius:50%;display:block}
.nav{position:absolute;top:62px;left:394px;display:flex;gap:14px;font-size:12px;font-weight:500}
.burger{position:absolute;left:996px;top:63px;width:18px}
.burger i{display:block;height:2px;background:#fff;margin-bottom:4px}
.hero h1{position:absolute;left:184px;top:158px;font-size:50px;line-height:58px}
.hero p{position:absolute;left:184px;top:306px;font-size:14px;line-height:23px}

/* partners */
.partners{top:650px;height:80px;display:flex;justify-content:space-between;padding:0 186px;align-items:center;color:#9a9a9a;font-size:22px;font-weight:600}

/* about */
.about{top:780px;height:520px}
.photo{position:absolute}
.dots{position:absolute;display:grid;gap:12px}
.dots i{width:4px;height:4px;border-radius:50%;background:#ccd}

/* services */
.services{top:1313px;height:499px;background:var(--light)}
.card{position:absolute;top:194px;width:262px;height:220px;background:var(--white);border-radius:4px;padding:28px 26px}
.card .ico{width:44px;height:44px;border-radius:6px;background:#eceef7;margin-bottom:20px;display:flex;align-items:center;justify-content:center}
.card h3{font-size:14px;font-weight:600;margin-bottom:12px}
.card p{font-size:11px;line-height:18px;color:#999;margin-bottom:10px}
.card a{font-size:11px;font-weight:600;color:var(--blue)}
.card.active{background:var(--blue);color:var(--white)}
.card.active p,.card.active a{color:#e6e8ff}
.card.active .ico{background:var(--white)}
.arrows{position:absolute;top:82px;left:943px;display:flex;gap:17px}
.arrows i{width:28px;height:28px;border-radius:50%;background:var(--white);display:flex;align-items:center;justify-content:center;font-style:normal;font-size:12px;box-shadow:0 2px 6px rgba(0,0,0,.08)}
.arrows i.on{background:var(--blue);color:#fff}

/* why */
.why{top:1812px;height:644px}
.checks{position:absolute;left:184px;top:340px;font-size:18px;color:#333}
.checks div{display:flex;align-items:center;gap:28px;height:48px}

/* contact */
.contact{top:2456px;height:560px}
.contact-bg{position:absolute;left:0;top:0;width:1200px;height:391px;background:linear-gradient(90deg,#1b1f55,#2c2a55 40%,#1b1d4d 80%,#0d0f52)}
.form{position:absolute;left:212px;top:214px;width:499px;height:341px;background:var(--white);box-shadow:0 10px 30px rgba(0,0,0,.08);padding:28px 46px}
.form h3{font-size:19px;font-weight:500;margin-bottom:30px}
.field{position:absolute}
.field small{display:block;font-size:11px;color:#888;margin-bottom:6px}
.field span{font-size:16px}
.info{position:absolute;left:711px;top:214px;width:285px;height:341px;background:var(--blue);color:var(--white);padding:28px 20px}
.info h3{font-size:19px;font-weight:600;margin-bottom:10px}
.info p{font-size:11px;line-height:18px;margin-bottom:18px}
.info .row{display:flex;gap:18px;font-size:14px;line-height:22px;margin-bottom:22px}

/* blog */
.blog{top:3060px;height:700px}
.post{position:absolute;top:156px;width:262px;height:390px;background:#f8f8f8}
.post .img{height:206px}
.post h3{font-size:14px;font-weight:600;line-height:20px;margin:28px 26px 12px}
.post p{font-size:11px;line-height:18px;color:#888;margin:0 26px 14px}
.post a{font-size:11px;font-weight:600;margin-left:26px}

/* footer */
.footer{top:3793px;height:552px;background:var(--footer);color:var(--white)}
.footer h2{position:absolute;left:184px;top:72px;font-size:30px;line-height:42px}
.news{position:absolute;left:592px;top:75px;width:425px;height:72px;border-radius:36px;background:var(--white);display:flex;align-items:center;padding:0 8px 0 40px;color:#aaa;font-size:14px}
.news .btn{position:relative;margin-left:auto;width:118px;height:46px;border-radius:23px;font-family:"Libre Baskerville",serif;font-size:13px}
.fcol{position:absolute;top:232px;font-size:12px;line-height:30px}
.fcol h4{font-size:14px;font-weight:600;margin-bottom:14px}
</style>
</head>
<body>

<header class="hero">
  <div class="hero-art" role="img" aria-label="Glowing blue globe with network connection lines"></div>
  <div class="topbar">
    <span style="left:184px">☏ &nbsp;(00) 555-0142</span>
    <span style="left:330px">✉ &nbsp;hello@vantrelworks.example</span>
    <span style="left:848px">Follow us on</span>
    <div class="social" style="left:938px;top:12px"><i></i><i></i><i></i><i></i></div>
  </div>
  <div class="brand" style="left:184px;top:52px"><b style="background:#fff"></b>Vantrel Works</div>
  <nav class="nav"><span>Home</span><span>About us</span><span>Contacts</span><span>Partners</span><span>Blog</span><span>Services</span><span>Resources</span><span>Technologies</span><span>Careers</span></nav>
  <div class="burger"><i></i><i></i><i></i></div>
  <h1 class="serif">Cyber Security Is<br>Not Optional</h1>
  <p>Lorem ipsum dolor sit amet, consectetur adipisi<br>cin sed do eiusmod tempor incidi.</p>
  <div class="btn" style="left:184px;top:389px;width:142px;height:57px;background:#fff;color:#111">Our Services</div>
  <div class="btn" style="left:347px;top:389px;width:142px;height:57px;border:1.5px solid #fff;color:#fff">Contact us</div>
</header>

<section class="partners">
  <span>Ostrav</span><span>Kelmo</span><span>Tunnelo</span><span>Brisket</span><span>Quorra</span><span>Lumin</span>
</section>

<section class="about">
  <div class="dots" style="left:140px;top:290px;grid-template-columns:repeat(2,4px);column-gap:18px;row-gap:33px">
    <i></i><i></i><i></i><i></i><i></i><i></i><i></i><i></i><i></i><i></i>
  </div>
  <div class="dots" style="left:140px;top:475px;grid-template-columns:repeat(9,4px);column-gap:18px"><i></i><i></i><i></i><i></i><i></i><i></i><i></i><i></i><i></i></div>
  <div class="photo" role="img" aria-label="Smiling woman on a sofa with a laptop holding a bank card" style="left:186px;top:17px;width:371px;height:438px;background:linear-gradient(160deg,#ece9e4,#b8b2aa 55%,#6d6a68)"></div>
  <div class="eyebrow abs" style="left:613px;top:15px;font-size:14px">About Us</div>
  <h2 class="serif abs" style="left:613px;top:50px;font-size:32px;line-height:40px">Protect Your Data And<br>Application</h2>
  <p class="para abs" style="left:613px;top:152px;width:370px">Lorem ipsum dolor sit amet, consectetur adipisi cing elit, sed do eiusmod tempor incididunt ut labore et dolore magna aliqua. Ut enim ad min im veniam, quis nostrud exercitation ullamco labo ris nisi ut aliquip ex ea commodo conse quat. Duis aute irure dolor in reprehenderit in voluptate olore eu fugiat nulla.</p>
  <div class="btn btn-blue" style="left:613px;top:343px;width:142px;height:57px">More About Us</div>
</section>

<section class="services">
  <div class="eyebrow abs" style="left:186px;top:82px">Our Services</div>
  <h2 class="serif abs" style="left:184px;top:120px;font-size:31px">What We Offer</h2>
  <div class="arrows"><i>‹</i><i class="on">›</i></div>
  <div class="card active" style="left:184px">
    <div class="ico"><svg width="20" height="20" viewBox="0 0 20 20" fill="none" stroke="#2b3597" stroke-width="1.5"><rect x="3" y="3" width="8" height="6"/><path d="M7 9v4M3 17h14M10 13h6v4"/></svg></div>
    <h3>Consulting</h3><p>Lorem ipsum dolor sit amet, co nsec tetur adipisicing elit, sed do eiusmod tempor.</p><a>Read More &nbsp;⟶</a>
  </div>
  <div class="card" style="left:469px">
    <div class="ico"><svg width="20" height="20" viewBox="0 0 20 20" fill="none" stroke="#555" stroke-width="1.5"><rect x="3" y="5" width="14" height="10"/><circle cx="10" cy="10" r="2"/></svg></div>
    <h3>Vulnerability Assessment</h3><p>Lorem ipsum dolor sit amet, cons ectetur adipisicing elit, sed do eiu sm od tempor incididunt.</p><a>Read More &nbsp;⟶</a>
  </div>
  <div class="card" style="left:753px">
    <div class="ico" style="border-radius:50%"><svg width="20" height="20" viewBox="0 0 20 20" fill="none" stroke="#555" stroke-width="1.5"><circle cx="10" cy="10" r="7"/><circle cx="10" cy="10" r="3"/></svg></div>
    <h3>ISO Compliance</h3><p>Lorem ipsum dolor sit amet, cons ectetur adipisicing elit, sed do eiu sm od tempor incididunt.</p><a>Read More &nbsp;⟶</a>
  </div>
</section>

<section class="why">
  <div class="eyebrow abs" style="left:186px;top:78px">Why Choose Us</div>
  <h2 class="serif abs" style="left:184px;top:115px;font-size:31px;line-height:48px">Provide Advanced Security<br>For Advanced Threat</h2>
  <p class="para abs" style="left:184px;top:228px;width:360px">Lorem ipsum dolor sit amet, consectetur adip iscing elit, sed do eiusmod tempor incididunt ut labore et dolore magna aliqua.</p>
  <div class="checks">
    <div><svg width="22" height="18" viewBox="0 0 22 18"><path d="M2 9l6 6L20 2" fill="none" stroke="#3cbf4a" stroke-width="4"/></svg>Content Delivery Network</div>
    <div><svg width="22" height="18" viewBox="0 0 22 18"><path d="M2 9l6 6L20 2" fill="none" stroke="#3cbf4a" stroke-width="4"/></svg>24/7 Support abd remote Admit</div>
    <div><svg width="22" height="18" viewBox="0 0 22 18"><path d="M2 9l6 6L20 2" fill="none" stroke="#3cbf4a" stroke-width="4"/></svg>Affordable price</div>
  </div>
  <div class="btn btn-blue" style="left:184px;top:513px;width:143px;height:57px;background:#211b9e">Learn More</div>
  <div class="photo" role="img" aria-label="Three business colleagues reviewing a tablet together" style="left:640px;top:79px;width:376px;height:479px;background:linear-gradient(170deg,#bfc3c8,#8a8580 50%,#3a3534)"></div>
</section>

<section class="contact">
  <div class="contact-bg" role="img" aria-label="Dim office scene with a person, under a dark blue overlay"></div>
  <div class="abs" style="left:0;width:1200px;top:78px;text-align:center;color:#fff;font-size:15px">Contact Us</div>
  <h2 class="serif abs" style="left:0;width:1200px;top:120px;text-align:center;color:#fff;font-size:30px">Stay Connected With Us</h2>
  <div class="form">
    <h3>Send us a Massage</h3>
    <div class="field" style="left:49px;top:102px"><small>Your Name</small><span>John Doe</span></div>
    <div class="field" style="left:231px;top:102px"><small>Your Email id</small><span>johndoe@mail.example</span></div>
    <div class="field" style="left:49px;top:170px"><small>Phone Number</small><span>768 654 123</span></div>
    <div class="field" style="left:231px;top:170px"><small>Subject</small><span>lorem ipsum</span></div>
    <div class="field" style="left:49px;top:236px"><small>Massage</small><span>Type your massage....</span></div>
    <div class="abs" style="left:372px;top:256px;width:48px;height:48px;border-radius:50%;background:#fff;box-shadow:0 4px 12px rgba(0,0,0,.12);display:flex;align-items:center;justify-content:center;color:var(--blue);font-weight:600">→</div>
  </div>
  <div class="info">
    <h3>Contact Information</h3>
    <p>Lorem ipsum dolor sit amet consectetur adipisicing elitseddo. eiusmod tempor incididun.</p>
    <div class="row"><svg width="12" height="16" viewBox="0 0 12 16"><path d="M6 0a6 6 0 0 0-6 6c0 4 6 10 6 10s6-6 6-10a6 6 0 0 0-6-6z" fill="#fff"/><circle cx="6" cy="6" r="2" fill="#2b3597"/></svg><span>Lorem ipsum dolor sit<br>amet cons - 012</span></div>
    <div class="row"><svg width="12" height="14" viewBox="0 0 12 14"><path d="M1 1h3l1 3-2 1c1 2 2 3 4 4l1-2 3 1v3c-6 1-11-4-10-10z" fill="#fff"/></svg><span>(00) 555 0198</span></div>
    <div class="row"><svg width="12" height="12" viewBox="0 0 12 12"><rect y="2" width="12" height="9" fill="#fff"/><path d="M0 2l6 5 6-5" stroke="#2b3597" fill="none"/></svg><span>hello@vantrelworks.example</span></div>
  </div>
</section>

<section class="blog">
  <div class="abs" style="left:0;width:1200px;top:37px;text-align:center;font-size:14px;color:#444">Our News</div>
  <h2 class="serif abs" style="left:0;width:1200px;top:77px;text-align:center;font-size:31px">Our Latest Blog</h2>
  <div class="post" style="left:184px"><div class="img" role="img" aria-label="Hooded figure typing on a laptop in blue and purple light" style="background:linear-gradient(135deg,#2a2fa8,#6a2a8c 60%,#c2307a)"></div><h3>Five strategies too optimize clod</h3><p>Lorem ipsum dolor sit amet, consectetur adipiscing elit, sed</p><a>Read More &nbsp;<span style="color:var(--blue)">⟶</span></a></div>
  <div class="post" style="left:469px"><div class="img" role="img" aria-label="Person sitting at a desk facing a laptop with code" style="background:linear-gradient(135deg,#8a5a3e,#3a2a24 60%,#1d1d1d)"></div><h3>Cyber criminals publish stolen sepa data</h3><p>Lorem ipsum dolor sit amet, consectetur adipiscing elit, sed</p><a>Read More &nbsp;<span style="color:var(--blue)">⟶</span></a></div>
  <div class="post" style="left:753px"><div class="img" role="img" aria-label="Person wearing VR goggles amid green digital code" style="background:linear-gradient(135deg,#0f2a16,#2f6a3a 55%,#0b150c)"></div><h3>The security risk of changing package owners</h3><p>Lorem ipsum dolor sit amet, consectetur adipiscing elit, sed</p><a>Read More &nbsp;<span style="color:var(--blue)">⟶</span></a></div>
  <div class="btn btn-blue serif" style="left:528px;top:591px;width:144px;height:55px;font-size:15px;font-family:'Libre Baskerville',serif">View More</div>
</section>

<footer class="footer">
  <h2 class="serif">Get update by signup<br>Newsletter.</h2>
  <div class="news">✉ &nbsp;&nbsp;&nbsp;Enter your email<div class="btn btn-blue">Subscribe</div></div>
  <div class="abs" style="left:184px;top:191px;width:832px;height:1px;background:#4a4a4a"></div>
  <div class="brand" style="left:184px;top:233px;font-size:16px"><b style="background:#fff"></b>Vantrel Works</div>
  <p class="abs" style="left:186px;top:300px;font-size:11px;line-height:17px">Lorem ipsum dolor sit amet,<br>con sectetur adipisicing,<br>elited do eiusmod tempor.</p>
  <div class="social" style="left:186px;top:387px"><i></i><i></i><i></i><i></i></div>
  <div class="fcol" style="left:471px"><h4>Quick Links</h4>Home<br>About us<br>Contacts<br>Partners<br>Blog</div>
  <div class="fcol" style="left:621px"><h4>Help</h4>Services<br>Resources<br>Technologies<br>Careers</div>
  <div class="fcol" style="left:775px;width:245px"><h4>Contact Us</h4>☎ &nbsp;&nbsp;(01) 555 0111 / (02) 555 0122<br>✉ &nbsp;&nbsp;info@vantrelworks.example<br><div style="line-height:17px;margin-top:8px;padding-left:32px;text-indent:-32px">⌖ &nbsp;&nbsp;&nbsp;&nbsp;Lorem ipsum dolor sit amet, cons ectetur adipisicin.</div></div>
  <div class="abs" style="left:0;width:1200px;top:498px;text-align:center;font-size:11px">Copyright © 2021 All rights reserved</div>
</footer>

</body>
</html>
```